Young Accounting firm needing a captivating business card

We need a business card design that forces the person to look at the card because its either gold foil, plastic, or lettering pop up etc. We already have a logo with a specific gold color and we need to make it pop. We are an accounting firm. I need the words" accounting, payroll, licenses, audits, taxes" somewhere on the business card so as to describe what we do- preferably on the side where the logo is at.

Industry/Entity Type

Accounting

Contact Information for Business Card

Address 48276 9th Ave S Ste 305, Alder Bay, OR 98117
Business Phone (360)418-2096
Fax (360)418-2157
Office Cell Phone (360)586-7319

Font styles to use
Serif

Colors
85abd2

Requirements
Must have
• It should state
• "Accounting" "Taxes" "Audits" "Licenses" "Payroll"
Nice to have
• Matte with gold foil, different textures, With Either a textured ivory background or gray blue slate background
Should not have
• colorful colors

```html
<!DOCTYPE html>
<html lang="en">
<head>
<meta charset="UTF-8">
<title>Kestrel Ledger – Business Card</title>
<link rel="stylesheet" href="https://fonts.googleapis.com/css2?family=Lato:wght@400;700;900&display=swap">
<style>
  :root {
    --bg: #2b2c2e;
    --card: #0b0c0c;
    --gold: #c9a233;
    --silver: #8d8e90;
    --silver-dim: #6f7072;
    --text-soft: #c8c8c8;
  }
  * { margin: 0; padding: 0; box-sizing: border-box; }
  html, body { width: 1200px; height: 970px; overflow: hidden; }
  body {
    background: var(--bg);
    font-family: "Lato", Arial, sans-serif;
    display: flex;
    flex-direction: column;
    align-items: center;
    justify-content: center;
    gap: 50px;
  }
  .card {
    width: 700px;
    height: 400px;
    background: var(--card);
    box-shadow: 0 14px 30px rgba(0,0,0,0.55);
    position: relative;
  }

  /* Front: contact side */
  .card--front { display: flex; align-items: center; }
  .front-brand {
    width: 330px;
    display: flex;
    align-items: center;
    justify-content: center;
    gap: 12px;
  }
  .brand-mark { width: 22px; height: 22px; background: var(--gold); }
  .brand-name {
    color: var(--gold);
    font-weight: 700;
    font-size: 34px;
    letter-spacing: 0.5px;
  }
  .divider {
    width: 1px;
    height: 230px;
    background: var(--gold);
  }
  .contact { padding-left: 34px; color: var(--text-soft); }
  .contact-name {
    color: var(--gold);
    font-weight: 900;
    font-size: 27px;
    line-height: 1.05;
  }
  .contact-role { font-size: 15px; margin-bottom: 14px; }
  .contact-address { font-size: 15px; line-height: 1.3; margin-bottom: 12px; }
  .contact-list { list-style: none; font-size: 15px; line-height: 1.5; }
  .contact-list li { display: flex; align-items: center; gap: 12px; }
  .contact-list svg { width: 16px; height: 16px; fill: var(--gold); flex: none; }

  /* Back: brand side */
  .card--back {
    display: flex;
    flex-direction: column;
    align-items: center;
    justify-content: center;
    gap: 14px;
  }
  .back-brand { display: flex; align-items: center; gap: 18px; }
  .back-brand .brand-mark { width: 40px; height: 40px; background: var(--silver); }
  .back-brand .brand-name { color: var(--silver); font-size: 60px; }
  .services {
    color: var(--silver-dim);
    font-size: 17px;
    letter-spacing: 0.8px;
    word-spacing: 4px;
  }
</style>
</head>
<body>

  <section class="card card--front">
    <div class="front-brand">
      <span class="brand-mark"></span>
      <span class="brand-name">Kestrel Ledger</span>
    </div>
    <div class="divider"></div>
    <div class="contact">
      <p class="contact-name">Daniel Whitford</p>
      <p class="contact-role">Founder</p>
      <p class="contact-address">48276 9th Ave S Ste 305,<br>Alder Bay, OR 98117</p>
      <ul class="contact-list">
        <li>
          <svg viewBox="0 0 16 16" aria-hidden="true"><path d="M4 1h8v14H4z M5.5 2.5v9h5v-9z M7 12.5h2v1H7z" fill-rule="evenodd"/></svg>
          (360) 586-7319
        </li>
        <li>
          <svg viewBox="0 0 16 16" aria-hidden="true"><path d="M1 5c0-2 3-3 7-3s7 1 7 3v1h-3V5H4v1H1z M3 7h10l1 7H2z"/></svg>
          (360) 418-2096
        </li>
        <li>
          <svg viewBox="0 0 16 16" aria-hidden="true"><path d="M4 1h8v4H4z M1 6h14v6h-3v3H4v-3H1z M5 10v4h6v-4z" fill-rule="evenodd"/></svg>
          (360) 418-2157
        </li>
        <li>
          <svg viewBox="0 0 16 16" aria-hidden="true"><path d="M1 3h14v10H1z M2.5 4.5 8 9l5.5-4.5z" fill-rule="evenodd"/></svg>
          daniel@kestrelledger.com
        </li>
      </ul>
    </div>
  </section>

  <section class="card card--back">
    <div class="back-brand">
      <span class="brand-mark"></span>
      <span class="brand-name">Kestrel Ledger</span>
    </div>
    <p class="services">Accounting | Taxes | Audits | Licenses | Payroll</p>
  </section>

</body>
</html>
```